Cleaning Company needs a new business card design

Hi, We are looking for new business card designs to update with our latest logo and company information.
We would like to see designs using the colours:
Royal Blue #4169E1 - this is our company colour so this has to be in there. Please feel free to experiment with other colours.
Must include:
Front of business card:
Logo
Back of the business card:
0800 519 2867
07946 581 302
Email: info@pelvormaids.co.uk
Web: www.pelvormaids.co.uk
Services:
End of Tenancy
Carpet & Upholstery
Regular & One Off
all work fully insured.
The front of the business card with the logo can be made to look raised print. The blue man to be a shiny finish.
The business card needs to be presented in a matt finish
The business must be in the following styles:
Standard Square with rounded corners.
Thank you to all that take part in this.
Target Market(s)
Men and Women of different ages in the UK.
Industry/Entity Type
House Cleaning
Contact Information for Business Card
Front of business card:
Logo
0800 519 2867
07946 581 302
Email: pelvormaids@brimmail.co.uk
Services:
End of Tenancy
Carpet & Upholstery
Regular & One Off
all work fully insured.

```html
<!DOCTYPE html>
<html lang="en">
<head>
<meta charset="utf-8">
<title>Pelvor Maids – Business Card</title>
<link rel="stylesheet" href="https://fonts.googleapis.com/css2?family=Fira+Sans:wght@400;500;600&display=swap">
<style>
  :root {
    --backdrop: #6a6763;
    --card-white: #ffffff;
    --brand-blue: #2e4a9a;
    --text-grey: #666666;
    --radius: 32px;
  }
  * { margin: 0; padding: 0; box-sizing: border-box; }
  html, body {
    width: 1200px;
    height: 1200px;
    overflow: hidden;
    background: var(--backdrop);
    font-family: "Fira Sans", sans-serif;
  }
  .canvas {
    position: relative;
    width: 1200px;
    height: 1200px;
  }
  .card {
    position: absolute;
    width: 677px;
    height: 387px;
    border-radius: var(--radius);
    overflow: hidden;
  }
  .card--back {
    left: 118px;
    top: 170px;
    background: var(--card-white);
  }
  .card--front {
    left: 406px;
    top: 643px;
    background: var(--brand-blue);
  }
  .side-tab {
    position: absolute;
    top: 128px;
    width: 38px;
    height: 131px;
  }
  .side-tab--left { left: 0; }
  .side-tab--right { right: 0; }
  .card--back .side-tab { background: var(--brand-blue); }
  .card--front .side-tab { background: var(--card-white); }

  .contact-list {
    position: absolute;
    left: 194px;
    top: 155px;
    display: grid;
    grid-template-columns: 53px auto;
    row-gap: 1px;
    font-size: 16.5px;
    line-height: 18.6px;
  }
  .contact-list dt {
    color: var(--brand-blue);
    font-weight: 500;
  }
  .contact-list dd {
    color: var(--text-grey);
    font-weight: 400;
    letter-spacing: 0.2px;
  }

  .brand-name {
    position: absolute;
    left: 0;
    right: 0;
    top: 50%;
    transform: translateY(-50%);
    text-align: center;
    color: var(--card-white);
    font-weight: 600;
    font-size: 54px;
    letter-spacing: -0.5px;
  }
</style>
</head>
<body>
  <main class="canvas">
    <section class="card card--back" aria-label="Business card back">
      <span class="side-tab side-tab--left"></span>
      <span class="side-tab side-tab--right"></span>
      <dl class="contact-list">
        <dt>Tel</dt><dd>: 0800 519 2867</dd>
        <dt>Mobile</dt><dd>: 07946 581 302</dd>
        <dt>Email</dt><dd>: info@pelvormaids.co.uk</dd>
        <dt>Web</dt><dd>: www.pelvormaids.co.uk</dd>
      </dl>
    </section>

    <section class="card card--front" aria-label="Business card front">
      <span class="side-tab side-tab--left"></span>
      <span class="side-tab side-tab--right"></span>
      <p class="brand-name">Pelvor Maids</p>
    </section>
  </main>
</body>
</html>
```